we need a homepage for a marketplace

We manage all projects using our ground-breaking platform Velbrim Portal. You get access to 150+ partners in 70 countries, security, cost efficiency, technical skills, speed, 100% visibility and accountability.Velbrim aims to help clients realize the full potential of their investments, provide a competitive price, establish the business need as a competitive advantage, and provide a strategic business asset that can facilitate growth.
Target Market(s)
Freelancers
Industry/Entity Type
Business Software
Number of Pages Required
1 page
Requirements
Must have
- Credentials -http://qlvtk.com/freelancer/public
- Front :
- Client:
- Email id - doriek@fallowquartzsystems.com
- Password - 123456
- Partner:
- Email id - mortenl@fallowquartzsystems.com
- Password - 123456
- Project Manager:
- Email id - lorcan@fallowquartzsystems.com
- Password - 123456
Nice to have
- It will be nice to have a creative design, and a outside the box look/feel

```html
<!DOCTYPE html>
<html lang="en">
<head>
<meta charset="utf-8">
<title>Velbrim – Contact</title>
<link rel="stylesheet" href="https://fonts.googleapis.com/css2?family=Open+Sans:wght@400;600&family=Raleway:wght@500;600;700&display=swap">
<style>
:root{
  --orange:#fe9800;
  --orange-text:#f7901e;
  --blue:#3ab6d6;
  --ink:#3a3a3a;
  --muted:#7a7a7a;
  --panel:#efefef;
  --footer:#3b3b3b;
  --logo:#2f4b5e;
  --white:#ffffff;
}
*{box-sizing:border-box;margin:0;padding:0}
html,body{width:1018px;height:1200px;overflow:hidden;background:var(--white)}
body{font-family:"Open Sans",sans-serif;color:var(--ink)}
.page{position:relative;width:1018px;height:1200px}
.abs{position:absolute}

/* header */
.brand{left:134px;top:24px;display:flex;align-items:center;gap:8px;font-family:"Raleway",sans-serif;font-weight:600;font-size:36px;color:var(--logo);line-height:1}
.brand-dot{width:14px;height:14px;border-radius:50%;background:var(--logo)}
.nav a{position:absolute;top:45px;font-family:"Raleway",sans-serif;font-weight:600;font-size:11px;color:#333;text-decoration:none;letter-spacing:.2px}
.nav a.active{color:var(--blue)}
.btn-add{left:793px;top:38px;width:88px;height:27px;background:var(--orange);color:#fff;font-family:"Raleway",sans-serif;font-weight:700;font-size:9.5px;display:flex;align-items:center;justify-content:center;border-radius:2px}

/* hero */
.hero{left:0;top:90px;width:1018px;height:275px;background:linear-gradient(100deg,#5a4538 0%,#8a5a34 35%,#a06a3c 55%,#7b5236 80%,#5e4a40 100%)}
.hero-title{left:138px;top:210px;font-family:"Raleway",sans-serif;font-weight:700;font-size:30px;color:#fff;letter-spacing:.3px}

/* intro */
.section-title{left:0;top:402px;width:1018px;text-align:center;font-family:"Raleway",sans-serif;font-weight:600;font-size:24px;color:var(--orange-text)}
.intro{left:150px;top:440px;width:718px;text-align:center;font-size:12.2px;line-height:19px;color:var(--muted)}

/* contact block */
.addresses{left:138px;top:510px;width:372px;height:332px;background:var(--panel)}
.addresses .divider{position:absolute;left:0;top:160px;width:372px;height:1px;background:#cfcfcf}
.office{position:absolute;left:34px}
.office h3{font-family:"Open Sans",sans-serif;font-weight:600;font-size:14px;color:#333;margin-bottom:7px}
.line{display:flex;align-items:flex-start;gap:7px;font-size:12px;line-height:17px;color:#333}
.line svg{flex:none;margin-top:2px}
.gap{margin-top:16px}

.form-panel{left:510px;top:510px;width:372px;height:332px;background:var(--orange)}
.form-panel h2{position:absolute;left:36px;top:26px;font-family:"Raleway",sans-serif;font-weight:500;font-size:17.5px;color:#fff}
.field{position:absolute;left:36px;width:307px;height:27px;background:linear-gradient(#fff,#f3f3f3);border:1px solid #e0e0e0;border-radius:2px;font-size:10px;color:#555;padding:7px 12px}
.field.tall{height:66px}
.field svg{position:absolute;right:9px;top:7px}
.submit{position:absolute;left:37px;top:278px;width:121px;height:32px;background:linear-gradient(#3a3a3a,#1c1c1c);color:#fff;font-family:"Raleway",sans-serif;font-weight:700;font-size:13px;display:flex;align-items:center;justify-content:center;letter-spacing:.4px}

/* footer */
.footer{left:0;top:918px;width:1018px;height:204px;background:var(--footer)}
.footer-divider{left:252px;top:922px;width:1px;height:200px;background:#555}
.footer-brand{left:138px;top:962px;display:flex;align-items:center;gap:6px;font-family:"Raleway",sans-serif;font-weight:600;font-size:22px;color:#fff}
.footer-brand span.dot{width:10px;height:10px;border-radius:50%;background:#fff}
.footer-about{left:138px;top:1017px;width:110px;font-size:10px;line-height:19.5px;color:#eee}
.col-title{font-family:"Raleway",sans-serif;font-weight:700;font-size:13px;color:#fff;top:950px}
.links{left:273px;top:975px;font-family:"Raleway",sans-serif;font-size:11.2px;line-height:17.8px;color:#ccc}
.post{width:170px}
.post h4{font-family:"Raleway",sans-serif;font-weight:600;font-size:11.4px;color:#ccc;margin-bottom:2px}
.post p{width:135px;font-size:9.2px;line-height:15px;color:#bbb}
.post .date{color:var(--orange)}
.news-text{left:722px;top:975px;width:135px;font-size:9.2px;line-height:15px;color:#bbb}
.news-input{left:722px;top:1014px;width:160px;height:29px;background:#fff;border-radius:2px;font-size:9px;color:#888;padding:9px 8px}
.news-btn{left:722px;top:1048px;width:77px;height:29px;background:var(--orange);color:#fff;border-radius:2px;font-family:"Raleway",sans-serif;font-weight:700;font-size:9px;display:flex;align-items:center;justify-content:center}

/* bottom band */
.band{left:0;top:1122px;width:1018px;height:78px;background:var(--blue)}
.legal{left:138px;top:1147px;font-size:9px;line-height:15.5px;color:#fff}
.band-name{left:678px;top:1154px;font-family:"Raleway",sans-serif;font-weight:700;font-size:16px;color:#d8eef5}
.social{left:773px;top:1151px;display:flex;gap:2px}
.social span{width:26px;height:26px;border-radius:50%;border:2px solid #fff;background:#2b6fa8}
.social span:nth-child(1){background:#4aa9dc}
.social span:nth-child(3){background:#1d6fa5}
.social span:nth-child(4){background:#d23c2e}
.page-code{left:911px;top:1162px;font-size:9px;color:#e6f5fa}
</style>
</head>
<body>
<div class="page">

  <header>
    <div class="abs brand"><span>Velbrim</span><span class="brand-dot"></span></div>
    <nav class="nav">
      <a style="left:403px">HOME</a>
      <a style="left:468px">HOW IT WORKS</a>
      <a style="left:582px">ABOUT</a>
      <a style="left:652px">CONTACT</a>
      <a class="active" style="left:736px">TEAM</a>
    </nav>
    <div class="abs btn-add">ADD PROJECT</div>
  </header>

  <section>
    <div class="abs hero" role="img" aria-label="Overhead photo of a team working at a wooden desk with laptops, keyboard and a small plant"></div>
    <h1 class="abs hero-title">GET IN TOUCH</h1>
  </section>

  <section>
    <h2 class="abs section-title">CONTACT US</h2>
    <p class="abs intro">Praesent elementum elit at tellus nec ultricies sit amet porttitor mattis enim In massa libero interdum nec interdum vel blandit sed<br>nulla In ullamcorper est eget tempor cursus neque mi consectetuer mi a ultricies</p>

    <div class="abs addresses">
      <div class="office" style="top:23px">
        <h3>USA ADDRESS</h3>
        <div class="line"><svg width="12" height="16" viewBox="0 0 12 16"><path d="M6 0C2.7 0 0 2.6 0 5.9 0 10 6 16 6 16s6-6 6-10.1C12 2.6 9.3 0 6 0zm0 8.3A2.4 2.4 0 1 1 6 3.5a2.4 2.4 0 0 1 0 4.8z" fill="#3ab6d6"/></svg><span>214 Harrow Bend Road Suite C12<br>Millbrook, PA 18902</span></div>
        <div class="line gap"><svg width="15" height="15" viewBox="0 0 16 16"><path d="M3.5 0.5l2.5 3.2-1.6 2a10 10 0 0 0 5.9 5.9l2-1.6 3.2 2.5-1.8 2.8C7.5 15.8 0.2 8.5 0.7 2.3z" fill="#3ab6d6"/></svg><span>(555) 014-2290</span></div>
        <div class="line"><svg width="16" height="12" viewBox="0 0 16 12"><rect width="16" height="12" rx="1" fill="#3ab6d6"/><path d="M0.5 1l7.5 6 7.5-6" stroke="#fff" stroke-width="1.4" fill="none"/></svg><span>info@velbrim-mail.com</span></div>
      </div>
      <div class="divider"></div>
      <div class="office" style="top:178px">
        <h3>UK ADDRESS</h3>
        <div class="line"><svg width="12" height="16" viewBox="0 0 12 16"><path d="M6 0C2.7 0 0 2.6 0 5.9 0 10 6 16 6 16s6-6 6-10.1C12 2.6 9.3 0 6 0zm0 8.3A2.4 2.4 0 1 1 6 3.5a2.4 2.4 0 0 1 0 4.8z" fill="#3ab6d6"/></svg><span>214 Harrow Bend Road Suite C12<br>Millbrook, PA 18902</span></div>
        <div class="line gap"><svg width="15" height="15" viewBox="0 0 16 16"><path d="M3.5 0.5l2.5 3.2-1.6 2a10 10 0 0 0 5.9 5.9l2-1.6 3.2 2.5-1.8 2.8C7.5 15.8 0.2 8.5 0.7 2.3z" fill="#3ab6d6"/></svg><span>(555) 014-2290</span></div>
        <div class="line"><svg width="16" height="12" viewBox="0 0 16 12"><rect width="16" height="12" rx="1" fill="#3ab6d6"/><path d="M0.5 1l7.5 6 7.5-6" stroke="#fff" stroke-width="1.4" fill="none"/></svg><span>info@velbrim-mail.com</span></div>
      </div>
    </div>

    <div class="abs form-panel">
      <h2>FILL OUR CONTACT FORM</h2>
      <div class="field" style="top:62px">Your name</div>
      <div class="field" style="top:96px">Email address</div>
      <div class="field" style="top:130px">Phone</div>
      <div class="field" style="top:166px">Upload FIle<svg width="15" height="12" viewBox="0 0 15 12"><path d="M9 0l6 5-6 5V7C4.5 7 2 8.5 0 12 0.8 6.5 3.5 3.5 9 3z" fill="#999"/></svg></div>
      <div class="field tall" style="top:202px">Message</div>
      <div class="submit">SUBMIT</div>
    </div>
  </section>

  <footer>
    <div class="abs footer"></div>
    <div class="abs footer-divider"></div>
    <div class="abs footer-brand"><span>Velbrim</span><span class="dot"></span></div>
    <p class="abs footer-about">Duis aute irure dolor in reprehenderit in volupt ate velit esse cillum...</p>

    <h5 class="abs col-title" style="left:272px">CAREER</h5>
    <div class="abs links">API<br>Mobile Apps<br>Downloads<br>Tutorials<br>FAQ</div>

    <h5 class="abs col-title" style="left:360px">EVENT</h5>
    <div class="abs post" style="left:361px;top:976px"><h4>Nemo enim ipsam voluptatem</h4><p>Tempora incidunt ut labore et magnam aliquam..<span class="date">23,July,2016</span></p></div>
    <div class="abs post" style="left:361px;top:1033px"><h4>Nemo enim ipsam voluptatem</h4><p>Tempora incidunt ut labore et magnam aliquam..<span class="date">23,July,2016</span></p></div>

    <h5 class="abs col-title" style="left:538px">BLOG</h5>
    <div class="abs post" style="left:540px;top:976px"><h4>Nemo enim ipsam voluptatem</h4><p>Tempora incidunt ut labore et magnam aliquam..<span class="date">23,July,2016</span></p></div>
    <div class="abs post" style="left:540px;top:1033px"><h4>Nemo enim ipsam voluptatem</h4><p>Tempora incidunt ut labore et magnam aliquam..<span class="date">23,July,2016</span></p></div>

    <h5 class="abs col-title" style="left:722px">NEWSLETTER</h5>
    <p class="abs news-text">Tempora incidunt ut labore et magnam aliquam..</p>
    <div class="abs news-input">E-mail Address</div>
    <div class="abs news-btn">SUBSCRIBE</div>

    <div class="abs band"></div>
    <p class="abs legal">© 2016 Velbrim.. All Copyrights are Reserved.<br>Privacy | Terms &amp; Conditions</p>
    <div class="abs band-name">Velbrim.</div>
    <div class="abs social" role="img" aria-label="Social network links"><span></span><span></span><span></span><span></span></div>
    <div class="abs page-code">C4</div>
  </footer>

</div>
</body>
</html>
```